Cobalt Skyway is an innovative offering which enables the mass market to book seats on private jets at commercial airline prices to destinations worldwide.

We need a lgog and Wordpress theme header for this initiative. Will like need other matrials but need these two images asap

Industry/Entity Type

Social

```html
<!DOCTYPE html>
<html lang="en">
<head>
<meta charset="utf-8">
<title>Cobalt Skyway</title>
<link href="https://fonts.googleapis.com/css2?family=Arimo:wght@400;700&display=swap" rel="stylesheet">
<style>
:root{
  --sky-top:#5fa9d6;
  --sky-mid:#8cc5e6;
  --sky-pale:#d6ecf8;
  --white:#ffffff;
  --nav-text:#3c7fb5;
  --link:#2d8fd0;
  --accent:#39a6dd;
  --text:#222222;
  --muted:#555555;
  --line:#c9d7e2;
  --panel:#e6f4fc;
  --footer:#f2f4f6;
}
*{box-sizing:border-box;margin:0;padding:0}
html,body{width:863px;height:1200px;overflow:hidden}
body{font-family:"Arimo",Arial,sans-serif;color:var(--text);background:var(--white)}
.page{position:relative;width:863px;height:1200px;overflow:hidden;
  background:linear-gradient(180deg,var(--sky-top) 0,var(--sky-mid) 300px,var(--sky-pale) 500px,#f4fafd 640px,var(--white) 760px)}
.abs{position:absolute}
.logo{left:45px;top:36px;font-size:40px;font-weight:700;color:var(--white);letter-spacing:.5px}
.account-tab{left:510px;top:88px;width:338px;height:36px;border-radius:14px 14px 0 0;background:rgba(255,255,255,.22)}
.account-links{left:527px;top:98px;font-size:11px;color:var(--white)}
.account-links a{color:var(--white)}
.account-links span{margin:0 6px}
.site-search{left:664px;top:93px;width:168px;height:23px;border-radius:12px;background:var(--white)}
.site-search svg{position:absolute;right:10px;top:6px}
.nav{left:17px;top:124px;width:829px;height:45px;border-radius:24px;
  background:linear-gradient(180deg,#ffffff 0,#eaf5fb 55%,#d3e8f4 100%);border:3px solid rgba(255,255,255,.7);box-shadow:0 1px 3px rgba(40,100,150,.25)}
.nav-item{top:138px;font-size:10.5px;font-weight:700;color:var(--nav-text)}
.nav-sep{top:134px;width:1px;height:22px;background:var(--line)}
.nav-active{left:27px;top:131px;width:66px;height:31px;border-radius:16px;background:linear-gradient(180deg,#7fc2e8,#4a9bcf);box-shadow:inset 0 1px 2px rgba(0,0,0,.15)}
.nav-active-label{left:27px;top:140px;width:66px;text-align:center;font-size:10.5px;font-weight:700;color:var(--white)}
.stage{left:21px;top:189px;width:819px;height:342px;border-radius:12px;background:rgba(255,255,255,.35)}
.search-box{left:36px;top:201px;width:271px;height:317px;border-radius:10px;background:linear-gradient(180deg,#ffffff,#e8f5fc);border:1px solid #c5dfef;font-size:8px;color:#444}
.search-box .abs{white-space:nowrap}
.sb-title{font-size:11px;font-weight:700;color:var(--link)}
.dots{height:0;border-top:1px dotted #b5c6d3}
.blue{color:var(--link)}
.uline{text-decoration:underline}
.field{height:17px;background:var(--white);border:1px solid #a9b9c5;color:#999;font-size:7.5px;padding:3px 3px}
.select-arrow{position:absolute;right:1px;top:1px;width:13px;height:13px;border:1px solid #889;background:#eef}
.radio{width:8px;height:8px;border-radius:50%;border:1px solid #777;background:#fff}
.radio.on::after{content:"";position:absolute;left:1.5px;top:1.5px;width:3px;height:3px;border-radius:50%;background:#333}
.check{width:8px;height:8px;border:1px solid #666;background:#fff}
.btn-search{width:60px;height:17px;border-radius:9px;border:1px solid #9bb8cc;background:linear-gradient(180deg,#fff,#dfeef7);text-align:center;font-size:8px;line-height:15px;color:#333}
.hero{left:315px;top:204px;width:510px;height:313px;border-radius:10px;overflow:hidden;
  background:linear-gradient(160deg,#4f86c9 0,#8fb9e2 30%,#c9ddf0 52%,#5e93cf 75%,#2c5fae 100%)}
.hero-caption{left:326px;top:228px;font-size:20px;line-height:25px;color:var(--white)}
.card{left:28px;top:561px;width:215px;height:399px;border-radius:10px;background:var(--white);border:1px solid #cfdde7}
.card-title{left:54px;top:578px;font-size:17px;color:#333}
.quote{font-size:10.5px;line-height:12.4px;color:#444;width:160px}
.t-name{font-size:10.5px;color:#444;text-align:right;width:150px}
.t-place{font-size:10.5px;color:var(--accent);text-align:right;width:150px}
.read-all{left:62px;top:921px;font-size:10.5px;color:var(--accent)}
.col-head{top:580px;font-size:15.5px;color:#222}
.thumb{top:604px;height:125px;border-radius:8px;border:3px solid #eef4f8}
.col-sub{top:749px;font-size:12px;color:var(--accent)}
.col-text{font-size:10.3px;line-height:12.4px;color:#111;width:150px}
.more{font-size:10.5px;color:var(--link);text-decoration:underline}
.find-flight{left:28px;top:975px;width:212px;height:185px;border-radius:9px;overflow:hidden;
  background:linear-gradient(180deg,#3e6fb0 0,#5c93c9 18%,#3f8aa8 45%,#2a5e86 75%,#1a3560 100%)}
.find-label{left:28px;top:1121px;width:212px;height:28px;background:rgba(255,255,255,.22)}
.find-text{left:56px;top:1125px;font-size:19px;color:var(--white)}
.welcome-title{left:280px;top:975px;font-size:14px;color:#222;letter-spacing:-.2px}
.welcome-text{left:282px;top:1008px;width:510px;font-size:11.2px;line-height:14.2px;color:#222}
.footer{left:0;top:1172px;width:863px;height:28px;background:var(--footer)}
.footer-text{left:669px;top:1183px;font-size:10.5px;color:var(--link)}
.footer-text a{color:var(--link)}
</style>
</head>
<body>
<div class="page">

  <header>
    <div class="abs logo">Cobalt Skyway</div>
    <div class="abs account-tab"></div>
    <div class="abs account-links"><a href="#">Register</a><span>|</span><a href="#">Clients Login</a></div>
    <div class="abs site-search">
      <svg width="10" height="10" viewBox="0 0 10 10"><circle cx="4" cy="4" r="3" fill="none" stroke="#333" stroke-width="1.3"/><line x1="6.2" y1="6.2" x2="9" y2="9" stroke="#333" stroke-width="1.5"/></svg>
    </div>
  </header>

  <nav>
    <div class="abs nav"></div>
    <div class="abs nav-active"></div>
    <div class="abs nav-active-label">ABOUT</div>
    <div class="abs nav-item" style="left:110px">FLIGTHS</div>
    <div class="abs nav-sep" style="left:158px"></div>
    <div class="abs nav-item" style="left:171px">HOLIDAYS</div>
    <div class="abs nav-sep" style="left:231px"></div>
    <div class="abs nav-item" style="left:243px">DEALS</div>
    <div class="abs nav-sep" style="left:291px"></div>
    <div class="abs nav-item" style="left:305px">FLIGHT GUIDE</div>
    <div class="abs nav-sep" style="left:388px"></div>
    <div class="abs nav-item" style="left:404px">INSURANCE</div>
    <div class="abs nav-sep" style="left:485px"></div>
    <div class="abs nav-item" style="left:503px">CAR HIRE</div>
    <div class="abs nav-sep" style="left:572px"></div>
    <div class="abs nav-item" style="left:591px">SUPPORT</div>
    <div class="abs nav-sep" style="left:660px"></div>
    <div class="abs nav-item" style="left:677px">SAFETY</div>
    <div class="abs nav-sep" style="left:731px"></div>
    <div class="abs nav-item" style="left:745px">CONTACTS</div>
  </nav>

  <section>
    <div class="abs stage"></div>
    <form class="abs search-box">
      <div class="abs sb-title" style="left:20px;top:18px">Flight Search</div>
      <div class="abs dots" style="left:20px;top:37px;width:217px"></div>
      <div class="abs radio on" style="left:24px;top:48px"></div>
      <div class="abs blue" style="left:36px;top:47px">Round Trip</div>
      <div class="abs radio" style="left:99px;top:48px"></div>
      <div class="abs blue" style="left:122px;top:47px">One Way</div>
      <div class="abs blue uline" style="left:172px;top:47px">Multiple Destinations</div>
      <div class="abs" style="left:26px;top:68px">From:</div>
      <div class="abs" style="left:153px;top:68px">To:</div>
      <div class="abs field" style="left:26px;top:80px;width:101px"></div>
      <div class="abs field" style="left:153px;top:80px;width:102px"></div>
      <div class="abs check" style="left:26px;top:108px"></div>
      <div class="abs" style="left:40px;top:107px">Search Nearby Airports</div>
      <div class="abs" style="left:26px;top:129px">Depart ( MM/DD/YYYY)</div>
      <div class="abs" style="left:154px;top:131px">Time:</div>
      <div class="abs field" style="left:26px;top:141px;width:101px">07/25/2010</div>
      <div class="abs field" style="left:153px;top:141px;width:102px">Anytime<span class="select-arrow"></span></div>
      <div class="abs" style="left:26px;top:165px">Return ( MM/DD/YYYY)</div>
      <div class="abs" style="left:154px;top:167px">Time:</div>
      <div class="abs field" style="left:26px;top:177px;width:101px">08/25/2010</div>
      <div class="abs field" style="left:153px;top:177px;width:102px">Anytime<span class="select-arrow"></span></div>
      <div class="abs dots" style="left:20px;top:207px;width:237px"></div>
      <div class="abs" style="left:26px;top:216px">Adults:</div>
      <div class="abs" style="left:89px;top:216px">Cabin:</div>
      <div class="abs field" style="left:26px;top:229px;width:39px;color:#333">1<span class="select-arrow"></span></div>
      <div class="abs radio on" style="left:90px;top:234px"></div>
      <div class="abs" style="left:103px;top:233px">Economy</div>
      <div class="abs radio" style="left:156px;top:234px"></div>
      <div class="abs" style="left:169px;top:233px">First/BusinessFi</div>
      <div class="abs" style="left:26px;top:253px">Search By:</div>
      <div class="abs check" style="left:26px;top:268px"></div>
      <div class="abs" style="left:41px;top:267px">Price</div>
      <div class="abs check" style="left:101px;top:268px"></div>
      <div class="abs" style="left:117px;top:267px">Schedule</div>
      <div class="abs check" style="left:181px;top:268px"></div>
      <div class="abs" style="left:197px;top:267px">Reward Travel</div>
      <div class="abs dots" style="left:20px;top:286px;width:237px"></div>
      <div class="abs blue uline" style="left:26px;top:293px">Advanced Search</div>
      <div class="abs" style="left:26px;top:305px">Children, Country of Purchase....</div>
      <div class="abs btn-search" style="left:186px;top:293px">SEARCH</div>
    </form>
    <div class="abs hero" role="img" aria-label="Photo of a jet airliner flying above white clouds">
      <div class="abs hero-caption">Great flights prices,<br>whatever your<br>destination</div>
    </div>
  </section>

  <aside>
    <div class="abs card"></div>
    <div class="abs card-title">Testimonials</div>
    <svg class="abs" style="left:191px;top:583px" width="12" height="11" viewBox="0 0 12 11"><ellipse cx="6" cy="4.5" rx="5.5" ry="4" fill="#bfe0f2" stroke="#5aa7d4"/><path d="M3 7.5 L2 10.5 L6 8" fill="#bfe0f2" stroke="#5aa7d4"/></svg>
    <div class="abs dots" style="left:31px;top:610px;width:209px"></div>
    <div class="abs quote" style="left:62px;top:640px">"lorem ipsum dolor sit amet, consectetuerelit,sed diam. lorem ipsum dolor sit amet. tetuer asipiscing elit."</div>
    <div class="abs t-name" style="left:62px;top:709px">Carl Denning</div>
    <div class="abs t-place" style="left:62px;top:725px">USA</div>
    <div class="abs dots" style="left:70px;top:744px;width:142px"></div>
    <div class="abs quote" style="left:62px;top:766px">"lorem ipsum dolor sit amet, consectetuerelit,sed diam. lorem ipsum dolor sit amet. tetuer asipiscing elit."</div>
    <div class="abs t-name" style="left:62px;top:835px">Mira Okafor</div>
    <div class="abs t-place" style="left:62px;top:851px">USA</div>
    <div class="abs dots" style="left:31px;top:906px;width:209px"></div>
    <div class="abs read-all"><span class="uline">Read All Testimonials </span> &gt;&gt;</div>

    <div class="abs find-flight" role="img" aria-label="Photo of an airliner silhouette landing at dusk"></div>
    <div class="abs find-label"></div>
    <div class="abs find-text">Find Best Flight &nbsp;&gt;</div>
  </aside>

  <main>
    <div class="abs col-head" style="left:281px">Plan Your Flight</div>
    <div class="abs thumb" style="left:274px;width:163px;background:linear-gradient(135deg,#ffffff,#e6e9ec)" role="img" aria-label="Airspace sector map"></div>
    <div class="abs col-sub" style="left:280px">lorem ipsum dolor sit amet</div>
    <div class="abs col-text" style="left:280px;top:772px">lorem ipsum dolor sit amet, consectetuerelit,sed diam. lorem ipsum dolor sit amet. tetuer asipiscing elit.</div>
    <div class="abs col-text" style="left:280px;top:828px">lorem ipsum dolor sit amet, consectetuerelit,sed diam. lorem ipsum dolor sit amet. tetuer asipiscing elit.</div>
    <div class="abs more" style="left:282px;top:896px">Read More</div>

    <div class="abs col-head" style="left:474px">Best Prices</div>
    <div class="abs thumb" style="left:464px;width:162px;background:linear-gradient(180deg,#3a6fc0,#7fa9dd 55%,#2d5aa4)" role="img" aria-label="Screenshot of a travel blog with an airliner"></div>
    <div class="abs col-sub" style="left:474px">lorem ipsum dolor sit amet</div>
    <div class="abs col-text" style="left:474px;top:772px">lorem ipsum dolor sit amet, consectetuerelit,sed diam. lorem ipsum dolor sit amet. tetuer asipiscing elit.</div>
    <div class="abs col-text" style="left:474px;top:828px">lorem ipsum dolor sit amet, consectetuerelit,sed diam. lorem ipsum dolor sit amet. tetuer asipiscing elit.</div>
    <div class="abs more" style="left:475px;top:896px">Read More</div>

    <div class="abs col-head" style="left:665px">Private Flights</div>
    <div class="abs thumb" style="left:654px;width:164px;background:linear-gradient(180deg,#b9714a,#d9c3a8 45%,#a8683f)" role="img" aria-label="Photo of a private jet cabin with leather seats"></div>
    <div class="abs col-sub" style="left:666px">lorem ipsum dolor sit amet</div>
    <div class="abs col-text" style="left:666px;top:772px">lorem ipsum dolor sit amet, consectetuerelit,sed diam. lorem ipsum dolor sit amet. tetuer asipiscing elit.</div>
    <div class="abs col-text" style="left:666px;top:828px">lorem ipsum dolor sit amet, consectetuerelit,sed diam. lorem ipsum dolor sit amet. tetuer asipiscing elit.</div>
    <div class="abs more" style="left:671px;top:896px">Read More</div>

    <div class="abs welcome-title">Welocme To Our Website!</div>
    <p class="abs welcome-text">lorem ipsum dolor sit amet, consectetuer asipiscing elit, sed diam.lorem ipsum dolor sit amet, consectetuer asipiscing elit, sed diam.lorem ipsum dolor sit amet, consectetuer asipiscing elit, sed diam.lorem ipsum dolor sit amet,consectetuer asipiscing elit, sed diam.<br>lorem ipsum dolor sit amet, consectetuer asipiscing elit, sed diam.lorem ipsum dolor sit amet, consectetuer asipiscing elit, sed diam.</p>
    <div class="abs more" style="left:726px;top:1106px">Read More</div>
  </main>

  <footer>
    <div class="abs footer"></div>
    <div class="abs footer-text">Skyway © 2010 &nbsp;| &nbsp;<a href="#">Privacy Policy</a></div>
  </footer>

</div>
</body>
</html>
```